MARLSTONE BUILDWORKS B-Card

I currently have a b-card design but will be removing the image (tree) from the logo and have text only.
I want the card to be classy and strong within the building and construction industry.
I will be using Spot UV on the cards as per the attached examples. I will also send through some sketched ideas that I have in mind.
The color blue is similar to the image (No. 6) attached images

Target Market(s)

middle to maturre aged.
Home Owners / Renovators and Builders

Industry/Entity Type

Construction

Contact Information for Business Card

MARLSTONE BUILDWORKS
Name: Gideon Pellow
Title: Project Manager
Mobile: 0472 315 084
Office: (08) 9571 2046
Address: 17C Quenby Parade, Bexmoor WA 6058
Email: info@marlstonehouses.example.au
PO Box: 3817 Bexmoor WA 6931

Colors
0592cd
33a6d7
85cae6
1b1b1b

Requirements
Must have
• 1. It must have spot UV on the front of card, maybe back of card too
• 2. I really like the blue on image 6. (or at least a really cool electric blue against the charcoal grey background)
• 3. The font must be slimline and modern. Easy to read
• 4. There must be no black used on the card... Only greys and dark charcoal greys
• 5. Use only the text from the logo "Marlstone Buildworks" Not the image of the tree. I am wanting the b-cards to be more masculine.
Nice to have
• 1. I like the design concept on image 6. but happy to see what else you can do with the Spot UV
• 2. Unless you have a really cool idea of the image of the tree (from previous logo) Spot UV somewhere in the design concept thats original and different then I am keen to see what you come up with
• 3. Try changing the color of the logo eg. full white or Blue and white
• 4. Another option is to have the Marlstone Logo on the front of card with the spot UV in the background of text which we specialise in eg, Roofing, Ceiling, Insulation, Gutter Guards, Electrical, Insurance etc and we can add or reduce items as required. Similar to image 12.
Should not have
• Do not include the image of the tree from previous logo. unless you have a really cool idea of Spot UV somewhere in the design concept thats original and different.

```html
<!DOCTYPE html>
<html lang="en">
<head>
<meta charset="utf-8">
<title>Marlstone Buildworks – Business Card Concepts</title>
<link rel="stylesheet" href="https://fonts.googleapis.com/css2?family=Jost:wght@300;400;500&family=Michroma&family=Noto+Serif:wght@400&display=swap">
<style>
  :root {
    --frame-blue: #2c6d95;
    --stage: #000000;
    --card-edge: #ffffff;
    --electric-blue: #0592cd;
    --mid-blue: #33a6d7;
    --pale-blue: #85cae6;
    --charcoal-blue: #2e5874;
    --white: #ffffff;
  }
  * { margin: 0; padding: 0; box-sizing: border-box; }
  html, body { width: 1200px; height: 670px; overflow: hidden; background: var(--stage); }

  .sheet {
    position: relative;
    width: 1200px; height: 670px;
    background: var(--stage);
    border: 5px solid var(--frame-blue);
  }

  .card {
    position: absolute;
    width: 491px; height: 261px;
    overflow: hidden;
    color: var(--white);
  }
  .card--front { border: 2px solid var(--card-edge); }
  .card--front-shaded { left: 2px; top: 2px;
    background:
      radial-gradient(ellipse 70% 90% at 22% 20%, rgba(46,88,116,0.95) 0%, rgba(46,88,116,0.6) 45%, rgba(5,146,205,0) 80%),
      linear-gradient(135deg, #3a6585 0%, #1d7fb3 55%, var(--electric-blue) 100%);
  }
  .card--front-flat { left: 698px; top: 2px;
    background:
      repeating-linear-gradient(120deg, rgba(255,255,255,0) 0 14px, rgba(255,255,255,0.035) 14px 15px),
      var(--electric-blue);
  }
  .card--back { width: 489px; height: 260px; }
  .card--back-shaded { left: 0; top: 400px;
    background:
      radial-gradient(ellipse 45% 55% at 12% 15%, rgba(46,88,116,0.95) 0%, rgba(46,88,116,0) 100%),
      radial-gradient(ellipse 40% 60% at 10% 95%, rgba(46,88,116,0.85) 0%, rgba(46,88,116,0) 100%),
      radial-gradient(ellipse 50% 45% at 55% 5%, rgba(46,88,116,0.8) 0%, rgba(46,88,116,0) 100%),
      linear-gradient(120deg, #2f6a90 0%, #1784bd 60%, var(--electric-blue) 100%);
  }
  .card--back-services { left: 701px; top: 400px; width: 494px; }
  .services-texture {
    position: absolute; inset: 0;
    background:
      linear-gradient(150deg, rgba(133,202,230,0.25) 0%, rgba(5,146,205,0) 45%, rgba(51,166,215,0.2) 100%),
      var(--electric-blue);
  }

  .corner-fold { position: absolute; left: 0; bottom: 0; }

  .wordmark {
    position: absolute;
    font-family: "Jost", "Futura", sans-serif;
    color: var(--white);
    text-align: center;
    line-height: 1;
  }
  .wordmark__name { display: block; font-weight: 500; }
  .wordmark__sub { display: block; font-weight: 300; }

  .card--front .wordmark { left: 36px; top: 115px; width: 142px; }
  .card--front .wordmark__name { font-size: 20px; letter-spacing: -0.3px; }
  .card--front .wordmark__sub { font-size: 8.5px; letter-spacing: 4.4px; margin-top: 2px; padding-left: 4px; }

  .card--back .wordmark { left: 0; right: 0; top: 88px; }
  .card--back .wordmark__name { font-size: 50px; letter-spacing: -0.8px; }
  .card--back .wordmark__sub { font-size: 19px; letter-spacing: 14px; margin-top: 4px; padding-left: 14px; }

  .contact { position: absolute; left: 222px; top: 57px; }
  .contact__name {
    font-family: "Michroma", "Eurostile", sans-serif;
    font-size: 14.5px; letter-spacing: 0.2px; line-height: 1.2;
  }
  .contact__title {
    font-family: "Noto Serif", Georgia, serif;
    font-size: 8.5px; margin-top: 1px;
  }
  .contact__details {
    list-style: none;
    margin-top: 33px;
    font-family: "Noto Serif", Georgia, serif;
    font-size: 9.6px; line-height: 16.7px;
  }
</style>
</head>
<body>
<main class="sheet">

  <section class="card card--front card--front-shaded" aria-label="Front of card, shaded version">
    <svg class="corner-fold" width="130" height="120" viewBox="0 0 130 120" aria-hidden="true">
      <polygon points="0,2 0,120 118,120" fill="var(--white)"/>
      <polygon points="0,2 118,120 128,120 0,-8" fill="rgba(255,255,255,0.08)"/>
    </svg>
    <div class="wordmark"><span class="wordmark__name">MARLSTONE</span><span class="wordmark__sub">BUILDWORKS</span></div>
    <div class="contact">
      <h1 class="contact__name">GIDEON PELLOW</h1>
      <p class="contact__title">Project Manager</p>
      <ul class="contact__details">
        <li>Mobile: 0472 315 084</li>
        <li>Office: (08) 9571 2046</li>
        <li>Email: info@marlstonehouses.example.au</li>
        <li>PO Box: 3817 Bexmoor WA 6931</li>
        <li>Address: 17C Quenby Parade, Bexmoor WA 6058</li>
      </ul>
    </div>
  </section>

  <section class="card card--front card--front-flat" aria-label="Front of card, flat blue version">
    <svg class="corner-fold" width="130" height="120" viewBox="0 0 130 120" aria-hidden="true">
      <polygon points="0,2 0,120 118,120" fill="var(--white)"/>
      <polygon points="0,2 118,120 128,120 0,-8" fill="rgba(255,255,255,0.08)"/>
    </svg>
    <div class="wordmark"><span class="wordmark__name">MARLSTONE</span><span class="wordmark__sub">BUILDWORKS</span></div>
    <div class="contact">
      <h2 class="contact__name">GIDEON PELLOW</h2>
      <p class="contact__title">Project Manager</p>
      <ul class="contact__details">
        <li>Mobile: 0472 315 084</li>
        <li>Office: (08) 9571 2046</li>
        <li>Email: info@marlstonehouses.example.au</li>
        <li>PO Box: 3817 Bexmoor WA 6931</li>
        <li>Address: 17C Quenby Parade, Bexmoor WA 6058</li>
      </ul>
    </div>
  </section>

  <section class="card card--back card--back-shaded" aria-label="Back of card, shaded version">
    <div class="wordmark"><span class="wordmark__name">MARLSTONE</span><span class="wordmark__sub">BUILDWORKS</span></div>
  </section>

  <section class="card card--back card--back-services" aria-label="Back of card, services version">
    <div class="services-texture" role="img" aria-label="Spot UV typographic pattern of service words such as roofing, ceilings, guttering, electrical and metal work, tone on tone in blue"></div>
    <div class="wordmark"><span class="wordmark__name">MARLSTONE</span><span class="wordmark__sub">BUILDWORKS</span></div>
  </section>

</main>
</body>
</html>
```